Edgey, Modern Air Conditioning Website

Quill Brothers
current website - www.pemblyhub.nz
Facebook - www.facebook.com/quillbro

We really have no idea about webdesign etc we are Engineers not Graphic artists or creative writers. We really just want a edgy, modern website completed on our behalf

We can get pictures of projects as directed or happy for you to use stock images of Varnock Lumen NZ (Heatpumps) air conditioning and exposed ducting etc

we would like the website to be heavily based on the below website. I like what they have done with both the site and the app but obviously would need to suit Quill Brothers, snowflakes heating cooling etc etc Blue and white to match our logo etc

http://gullwharfrigs.co.nz/

Need links to contact page:
Quill Brothers
37 Carrow Lane
Petone
Wellington

0800 927 514 (0800QBROLTD)

Merit.h@qbroltd.co.nz

QUILL BROTHERS
SATISFACTION GAURANTEED

WHY CHOOSE QUILL BROTHERS
EXPERIENCE COUNTS

We have a team of nationally trained and qualified Refrigeration/HVAC/Electrical Engineers and Technicians based in Petone, Wellington offering services to Wellington, Manuwatu and the Wairarapa. We are factory trained and authorised to design, service and install all major brands including Varnock, Ostrel, Pelloran Electric, Vantrigo and Brundel units. We extend our installation warranty to match that of the manufacturer’s warranty and specialise in our own diagnostics and repair.

SATISFACTION GUARANTEE
We aim to please and I put my name behind our brand! We will take care of your project from start to finish and offer a unique experience with our 100% satisfaction Guarantee*. We will supply and install your system and if your system is not installed how it was explained or not up to a trades standard we will return to make any the necessary modifications free of charge. We back this service up with our 0% upfront strategy, the power is in your hands. We will only invoice you once the installation has been completed up to a QUILL BROTHERS standard.

LOW PRESSURE SALES
Nobody likes the vacuum salesmen’s techniques and neither do we. We will come to your home or business to provide a free measure and quote. Our experience will insure this is a quick and painless experience, you will be provided with expert advice from a qualified Refrigeration Engineer, not a car salesmen turned “Heating Guru”. We will follow up with an email providing our best price straight up, installation details and online brochures. We won’t bug you with repeated phone calls and inbox clogging emails. Once we receive confirmation we will issue you with an installation date and typically have your installation completed within 10 working days.

BRANDS
www.varnocklumen.co.nz
www.ostrel.co.nz
http://plumbair.co.nz/

SERVICES
Heatpumps/Air Conditioning – Heat pumps are the most efficient way of using electricity to heat your home, but some are more efficient than others. We will select the right model for your requirements taking into account the capacity required, the visual impact of the system, the style of system, air flow and obviously your personal preferences. We only install the highest quality brands that offer outstanding after sales support. Cassettes, Consoles, Under Ceilings, Ducted, Hiwalls, Multis… Confused? Give us a call.

COMMERCIAL
We have a growing Portfolio of clients that rely on us for their Commercial requirements. We have proven ourselves to be a force to be reckoned with to be able to think outside the square and come up with unique and cost effective solutions to heat and cool large areas.

CENTRAL HEATING
Ducted Heatpumps are the holy grail of central heating and guess what? They can also cool and dehumidify your home. Ducted Heatpumps are often overlooked or priced out of reach by less experienced salesmen as its not just a point and shoot approach. We pride ourselves in our work with Ducted systems, we are able to provide quick and economic quotations and can provide expert advice on all the extra options on Ducted systems with zone control, fresh air integration, positive pressure solutions. We use the best materials when it comes to insulated ducting, mounting equipment, drainage materials. Every system we design is designed with the lowest possible decibel reading, least amount of static pressure and maximum effieciency with the help of the very latest software available.

VENTILATION
Home ventilation is a very important part of insuring you have a nice dry home to maximise the efficiency of your Heat pump. Whilst HRV systems are not designed to Heat your house they are designed to keep it dry, provide fresh filtered air to ensure your home healthy and easy to heat. We offer a number of solutions from integrated ducted heatpump systems to balanced heat recovery systems and positive air systems.

TESTIMONIALS
http://www.swapyard.co.nz/Browse/Listing.aspx?id=517362081

Target Market(s)

Home Owners

Industry/Entity Type

Air Conditioning

Colors
33a6d7
ffffff

Requirements
Must have
• Could possibly use the 'O' from Quill Brothers logo throughout website - see business Card
Nice to have
• Bright & Crisp - White and Blue
• Would love to have our Logo used throughout the website.

```html
<!DOCTYPE html>
<html lang="en">
<head>
<meta charset="utf-8">
<title>Quill Brothers – Heat Pumps, Heating & Ventilation</title>
<link href="https://fonts.googleapis.com/css2?family=Montserrat:wght@400;600;700&family=Lato:ital,wght@0,400;0,700;1,400&display=swap" rel="stylesheet">
<style>
:root{
  --blue:#33a6d7;
  --blue-dark:#2a8fbb;
  --white:#ffffff;
  --ink:#222222;
  --grey:#888888;
  --light:#f1f1f1;
  --dark:#1d1d1d;
  --darker:#141414;
  --line:#cfcfcf;
}
*{margin:0;padding:0;box-sizing:border-box}
html,body{width:1200px;height:3327px;overflow:hidden}
body{font-family:"Lato",sans-serif;color:var(--ink);background:var(--white);position:relative}
.abs{position:absolute}
.heading{font-family:"Montserrat",sans-serif;font-weight:700;text-align:center;letter-spacing:.5px}
.divider{position:absolute;left:50%;width:260px;height:12px;transform:translateX(-50%)}
.divider::before{content:"";position:absolute;left:0;right:0;top:5px;height:1px;background:var(--line)}
.divider::after{content:"";position:absolute;left:50%;top:0;width:12px;height:12px;margin-left:-6px;border-radius:50%;background:var(--grey);box-shadow:0 0 0 3px var(--white)}
.divider.on-dark::before{background:#666}
.divider.on-dark::after{background:#bbb;box-shadow:0 0 0 3px #2a2a2a}
.divider.on-blue::before{background:#8fd0ec}
.divider.on-blue::after{background:#e6f5fc;box-shadow:0 0 0 3px var(--blue)}

/* header / hero */
.hero{left:0;top:0;width:1200px;height:590px;background:linear-gradient(160deg,#d9d8d4 0%,#b7b4ad 35%,#8e8a83 65%,#5e5b56 100%)}
.brand{left:78px;top:26px;color:var(--white);font-family:"Montserrat",sans-serif;font-weight:700;font-size:44px;line-height:1;letter-spacing:1px}
.brand-sub{left:80px;top:78px;color:var(--white);font-family:"Montserrat",sans-serif;font-weight:700;font-size:14px;letter-spacing:9px}
.top-contact{top:22px;color:var(--white);font-size:17px;display:flex;align-items:center;gap:10px}
.top-contact .dot{width:30px;height:30px;border-radius:50%;background:var(--blue);display:flex;align-items:center;justify-content:center}
.nav{right:70px;top:80px;display:flex;gap:52px;font-family:"Montserrat",sans-serif;font-weight:600;font-size:14px;color:var(--white)}
.nav span.active{position:relative}
.nav span.active::after{content:"";position:absolute;left:50%;top:28px;width:8px;height:8px;margin-left:-4px;border-radius:50%;background:var(--white)}
.hero-title{left:0;width:1200px;top:458px;text-align:center;color:var(--white);font-family:"Montserrat",sans-serif;font-weight:600;font-size:32px;line-height:46px;text-shadow:0 2px 6px rgba(0,0,0,.5)}
.slide-arrow{top:275px;width:36px;height:46px;background:rgba(255,255,255,.85);display:flex;align-items:center;justify-content:center}

/* welcome */
.welcome-title{left:0;width:1200px;top:622px;font-size:31px;color:var(--ink)}
.welcome-title em{font-style:normal;color:var(--blue)}
.welcome-title b{font-weight:400;color:#777}
.welcome-text{left:100px;width:1000px;top:714px;text-align:center;font-size:15px;line-height:24px;color:#333}
.btn-more{left:533px;top:811px;width:132px;height:40px;border-radius:20px;background:var(--blue);color:var(--white);font-size:14px;font-weight:700;display:flex;align-items:center;padding-left:18px;gap:16px}
.btn-more i{width:30px;height:30px;border-radius:50%;background:#1b1b1b;display:flex;align-items:center;justify-content:center}

/* why choose */
.why{left:0;top:894px;width:1200px;height:481px;background:linear-gradient(180deg,#3b3b3b 0%,#1f1f1f 55%,#2b2b2b 100%)}
.notch{position:absolute;left:50%;width:0;height:0;margin-left:-26px;border-left:26px solid transparent;border-right:26px solid transparent}
.why-title{left:0;width:1200px;top:950px;font-size:29px;color:var(--white)}
.feature{top:1076px;width:330px;text-align:center;color:var(--white)}
.feature .ring{width:134px;height:134px;margin:0 auto;border-radius:50%;background:#d9d9d9;display:flex;align-items:center;justify-content:center}
.feature .core{width:88px;height:88px;border-radius:50%;background:#2b2b2b;display:flex;align-items:center;justify-content:center}
.feature h3{font-family:"Montserrat",sans-serif;font-weight:700;font-size:19px;margin-top:34px;letter-spacing:.5px}
.feature p{font-size:13px;line-height:21px;margin-top:10px;color:#e6e6e6}
.feature p span{color:var(--blue)}

/* services */
.services{left:0;top:1375px;width:1200px;height:528px;background:var(--light)}
.services-title{left:0;width:1200px;top:1433px;font-size:29px;color:#777}
.services-title em{font-style:normal;color:var(--blue)}
.hub{left:462px;top:1549px;width:274px;height:274px;border-radius:50%;background:var(--white);border:2px dashed #bdbdbd;display:flex;flex-direction:column;align-items:center;justify-content:center}
.hub .name{font-family:"Montserrat",sans-serif;font-weight:700;font-size:34px;color:var(--blue);letter-spacing:1px}
.hub .sub{font-family:"Montserrat",sans-serif;font-weight:700;font-size:11px;color:var(--blue);letter-spacing:6px;margin-top:2px}
.svc-icon{width:92px;height:92px;border-radius:50%;background:var(--white);box-shadow:0 2px 6px rgba(0,0,0,.15);display:flex;align-items:center;justify-content:center}
.svc-icon i{width:74px;height:74px;border-radius:50%;background:var(--blue);display:flex;align-items:center;justify-content:center}
.svc-label{font-family:"Montserrat",sans-serif;font-weight:700;font-size:21px;line-height:26px;color:#1d1d1d}
.connector{position:absolute;left:0;top:0}

/* gallery */
.gallery{left:0;top:1903px;width:1200px;height:364px;background:var(--blue)}
.gallery-title{left:0;width:1200px;top:1940px;font-size:29px;color:var(--white)}
.shot{top:2043px;width:250px;height:160px;border:3px solid var(--white)}
.shot-cap{top:2212px;width:250px;text-align:center;color:var(--white);font-size:13px;font-weight:700}
.gal-arrow{top:2108px;color:var(--white)}

/* testimonials */
.testi-title{left:0;width:1200px;top:2302px;font-size:29px;color:#777}
.testi-title em{font-style:normal;color:var(--blue)}
.avatar{width:116px;height:116px;border-radius:50%;border:4px solid var(--blue)}
.quote{font-size:14px;line-height:24px;font-style:italic;color:#333}
.quote .mark{color:var(--blue);font-size:38px;font-style:normal;line-height:10px;font-family:Georgia,serif;vertical-align:-14px;margin-right:8px}
.who{font-size:13px;color:var(--blue)}
.testi-rule{height:1px;background:#d8d8d8}
.pager{top:2610px;left:1075px;display:flex;gap:6px}
.pager i{width:9px;height:9px;border-radius:50%;background:#cfcfcf}
.pager i.on{background:var(--blue)}

/* contact */
.contact{left:0;top:2655px;width:1200px;height:512px;background:linear-gradient(180deg,#262626,#1a1a1a)}
.contact-title{left:0;width:1200px;top:2722px;font-size:31px;color:var(--white)}
.contact-sub{left:0;width:1200px;top:2804px;text-align:center;color:#dcdcdc;font-size:17px}
.contact-rule{left:100px;top:2842px;width:992px;height:1px;background:#3c3c3c}
.col-title{font-size:20px;color:#e4e4e4}
.field{left:100px;width:298px;height:28px;background:#111;border:1px solid #3a3a3a;color:#9a9a9a;font-size:12px;padding:6px 8px}
.send{left:97px;top:3092px;width:98px;height:30px;background:var(--blue);color:var(--white);font-family:"Montserrat",sans-serif;font-weight:700;font-size:14px;display:flex;align-items:center;justify-content:center}
.info{left:470px;color:#e4e4e4;font-size:13px;display:flex;align-items:flex-start;gap:14px}
.info svg{flex:none;margin-top:1px}
.socials{left:462px;top:3052px;display:flex;gap:12px}
.socials i{width:32px;height:32px;border-radius:50%;background:var(--blue)}
.contact-brand{left:843px;top:2918px;font-family:"Montserrat",sans-serif;font-weight:700;font-size:48px;color:#555;letter-spacing:1px;line-height:1}
.contact-brand-sub{left:850px;top:3005px;font-family:"Montserrat",sans-serif;font-weight:700;font-size:16px;color:#555;letter-spacing:12px}

/* newsletter / footer */
.newsletter{left:0;top:3167px;width:1200px;height:111px;background:var(--blue)}
.nl-icon{left:104px;top:3196px;width:54px;height:54px;border-radius:50%;border:3px solid var(--white);display:flex;align-items:center;justify-content:center}
.nl-title{left:176px;top:3204px;color:var(--white);font-family:"Montserrat",sans-serif;font-weight:600;font-size:27px}
.nl-input{left:496px;top:3203px;width:382px;height:40px;background:var(--white);font-size:13px;color:#333;padding:11px 10px}
.nl-btn{left:893px;top:3203px;width:196px;height:40px;background:#1f1f1f;color:var(--white);font-family:"Montserrat",sans-serif;font-weight:700;font-size:17px;letter-spacing:1px;display:flex;align-items:center;justify-content:center}
.footer{left:0;top:3278px;width:1200px;height:49px;background:#1a1a1a;color:#cfcfcf;font-size:13px;display:flex;align-items:center;justify-content:center}
</style>
</head>
<body>

<!-- header / hero -->
<div class="abs hero" role="img" aria-label="Photo of a woman relaxing on a sofa in a bright modern living room with a wall heat pump"></div>
<div class="abs brand">QUILL BROTHERS</div>
<div class="abs brand-sub">PETONE · WELLINGTON</div>
<div class="abs top-contact" style="left:752px">
  <span class="dot"><svg width="16" height="12" viewBox="0 0 16 12"><rect x="1" y="1" width="14" height="10" fill="none" stroke="#fff" stroke-width="1.6"/><path d="M1 1l7 6 7-6" fill="none" stroke="#fff" stroke-width="1.6"/></svg></span>
  merit.h@qbroltd.co.nz
</div>
<div class="abs top-contact" style="left:974px">
  <span class="dot"><svg width="14" height="14" viewBox="0 0 14 14"><path d="M3 1l2 3-1.5 1.5a8 8 0 0 0 5 5L10 9l3 2-1.5 2.5C6 13 1 8 .5 2.5z" fill="#fff"/></svg></span>
  022 418 3961
</div>
<nav class="abs nav"><span class="active">HOME</span><span>ABOUT US</span><span>SERVICES</span><span>GALLERY</span><span>CONTACT US</span></nav>
<h1 class="abs hero-title">We Have Installed Thousands Of Heat Pumps And<br>Also Specialise In Diagnostics And Repairs</h1>
<div class="abs slide-arrow" style="left:-8px"><svg width="10" height="14"><path d="M8 1L2 7l6 6" fill="none" stroke="#333" stroke-width="2"/></svg></div>
<div class="abs slide-arrow" style="left:1172px"><svg width="10" height="14"><path d="M2 1l6 6-6 6" fill="none" stroke="#333" stroke-width="2"/></svg></div>

<!-- welcome -->
<h2 class="abs heading welcome-title">WELCOME TO <em>QUILL</em> <b>BROTHERS</b></h2>
<div class="divider" style="top:678px"></div>
<p class="abs welcome-text">Purchasing a Heatpump or Ventilation System can be a significant investment but it doesnt have to be a daunting one. We have a team of nationally trained and qualified Refrigeration/HVAC/Electrical Engineers and Electricians. We are factory trained and authorised to service and install all major brands including Varnock, Kelvra, Ostrel and Pelloran Electric, Vantrigo and Brundel units. We have installed thousands of heat pumps and also specialise in diagnostics and repairs.</p>
<div class="abs btn-more">Read More <i><svg width="10" height="12"><path d="M2 1l6 5-6 5" fill="none" stroke="#fff" stroke-width="2"/></svg></i></div>

<!-- why choose -->
<section class="abs why" role="img" aria-label="Dark photo of exposed ceiling ducting in a commercial space">
  <div class="notch" style="top:0;border-top:22px solid var(--white)"></div>
  <div class="notch" style="bottom:-22px;border-top:22px solid #2b2b2b"></div>
</section>
<h2 class="abs heading why-title">WHY CHOOSE QUILL BROTHERS</h2>
<div class="divider on-dark" style="top:1010px"></div>

<div class="abs feature" style="left:100px">
  <div class="ring"><div class="core"><svg width="44" height="36" viewBox="0 0 44 36"><rect x="2" y="9" width="40" height="25" rx="3" fill="var(--blue)"/><rect x="15" y="2" width="14" height="8" rx="2" fill="none" stroke="var(--blue)" stroke-width="3"/></svg></div></div>
  <h3>EXPERIENCE COUNTS</h3>
  <p>We have a team of nationally trained and qualified Refrigeration/HVAC/Electrical Engineers and Technicians based in Petone...<span>[+]</span></p>
</div>
<div class="abs feature" style="left:435px">
  <div class="ring"><div class="core"><svg width="40" height="40" viewBox="0 0 40 40"><path d="M6 21l9 9L34 10" fill="none" stroke="var(--blue)" stroke-width="6" stroke-linecap="round" stroke-linejoin="round"/></svg></div></div>
  <h3>SATISFACTION GUARANTEE</h3>
  <p>We aim to please and I put my name behind our brand! We will take care of your project from start to finish and offer a unique experience...<span>[+]</span></p>
</div>
<div class="abs feature" style="left:770px">
  <div class="ring"><div class="core"><svg width="44" height="40" viewBox="0 0 44 40"><path d="M6 28a16 16 0 0 1 32 0" fill="none" stroke="var(--blue)" stroke-width="4"/><path d="M22 28l8-10" stroke="var(--blue)" stroke-width="4" stroke-linecap="round"/><rect x="4" y="33" width="36" height="4" fill="var(--blue)"/></svg></div></div>
  <h3>LOW PRESSURE SALES</h3>
  <p>Nobody likes the vacuum salesmen's techniques and neither do we. We will come to your home or business to provide a free measure ...<span>[+]</span></p>
</div>

<!-- services -->
<section class="abs services"></section>
<h2 class="abs heading services-title"><em>OUR</em> SERVICES</h2>
<div class="divider" style="top:1490px;--white:var(--light)"></div>

<svg class="connector" width="1200" height="3327" style="pointer-events:none">
  <g stroke="var(--blue)" stroke-width="2">
    <line x1="440" y1="1620" x2="474" y2="1640"/>
    <line x1="760" y1="1620" x2="724" y2="1640"/>
    <line x1="440" y1="1776" x2="474" y2="1756"/>
    <line x1="760" y1="1776" x2="724" y2="1756"/>
  </g>
  <g fill="var(--white)" stroke="var(--blue)" stroke-width="3">
    <circle cx="474" cy="1640" r="6"/><circle cx="724" cy="1640" r="6"/>
    <circle cx="474" cy="1756" r="6"/><circle cx="724" cy="1756" r="6"/>
  </g>
</svg>

<div class="abs hub">
  <div class="name">QUILL</div>
  <div class="sub">BROTHERS</div>
</div>

<div class="abs svc-icon" style="left:360px;top:1542px"><i><svg width="40" height="30" viewBox="0 0 40 30"><rect x="2" y="3" width="36" height="13" rx="2" fill="#fff"/><g stroke="#fff" stroke-width="2.5" stroke-linecap="round"><path d="M9 21v6M16 21v6M23 21v6M30 21v6"/></g></svg></i></div>
<div class="abs svc-label" style="left:150px;top:1560px;text-align:right;width:196px">Heatpumps/Air<br>Conditioning</div>

<div class="abs svc-icon" style="left:748px;top:1542px"><i><svg width="36" height="36" viewBox="0 0 36 36"><g fill="#fff"><rect x="5" y="6" width="5" height="24" rx="2"/><rect x="13" y="6" width="5" height="24" rx="2"/><rect x="21" y="6" width="5" height="24" rx="2"/><rect x="29" y="6" width="5" height="24" rx="2"/><rect x="2" y="26" width="34" height="3"/></g></svg></i></div>
<div class="abs svc-label" style="left:856px;top:1560px">Central<br>Heating</div>

<div class="abs svc-icon" style="left:360px;top:1762px"><i><svg width="34" height="36" viewBox="0 0 34 36"><rect x="4" y="4" width="18" height="30" fill="#fff"/><rect x="22" y="14" width="9" height="20" fill="#fff"/><g fill="var(--blue)"><rect x="8" y="9" width="4" height="4"/><rect x="14" y="9" width="4" height="4"/><rect x="8" y="17" width="4" height="4"/><rect x="14" y="17" width="4" height="4"/><rect x="10" y="26" width="6" height="8"/></g></svg></i></div>
<div class="abs svc-label" style="left:150px;top:1798px;text-align:right;width:196px">Commercial</div>

<div class="abs svc-icon" style="left:748px;top:1762px"><i><svg width="38" height="38" viewBox="0 0 38 38"><circle cx="19" cy="19" r="4" fill="#fff"/><g fill="#fff"><ellipse cx="19" cy="8" rx="5" ry="8"/><ellipse cx="19" cy="30" rx="5" ry="8"/><ellipse cx="8" cy="19" rx="8" ry="5"/><ellipse cx="30" cy="19" rx="8" ry="5"/></g></svg></i></div>
<div class="abs svc-label" style="left:856px;top:1798px">Ventilation</div>

<!-- gallery -->
<section class="abs gallery"></section>
<h2 class="abs heading gallery-title">PROJECT GALLERY</h2>
<div class="divider on-blue" style="top:1990px"></div>
<div class="abs gal-arrow" style="left:50px"><svg width="14" height="22"><path d="M12 2L3 11l9 9" fill="none" stroke="#fff" stroke-width="3"/></svg></div>
<div class="abs gal-arrow" style="left:1134px"><svg width="14" height="22"><path d="M2 2l9 9-9 9" fill="none" stroke="#fff" stroke-width="3"/></svg></div>

<div class="abs shot" style="left:82px;background:linear-gradient(160deg,#9a9ea2,#5c6166)" role="img" aria-label="Project photo of exposed ducting along a ceiling"></div>
<svg class="abs" style="left:188px;top:2104px" width="38" height="38"><circle cx="19" cy="19" r="17" fill="none" stroke="#fff" stroke-width="2"/><path d="M19 11v16M11 19h16" stroke="#fff" stroke-width="2"/></svg>
<div class="abs shot" style="left:344px;background:linear-gradient(160deg,#c08a5a,#6d4a30)" role="img" aria-label="Project photo of a restaurant interior with silver ducting"></div>
<div class="abs shot" style="left:608px;background:linear-gradient(160deg,#6f8f4a,#2f4a24)" role="img" aria-label="Project photo of rooftop ventilation units among greenery"></div>
<div class="abs shot" style="left:870px;background:linear-gradient(160deg,#c7c3bb,#8a877f)" role="img" aria-label="Project photo of an outdoor condenser unit beside a house"></div>
<div class="abs shot-cap" style="left:82px">Lorem Ipsum Dolor Sit</div>
<div class="abs shot-cap" style="left:344px">Lorem Ipsum Dolor Sit</div>
<div class="abs shot-cap" style="left:608px">Lorem Ipsum Dolor Sit</div>
<div class="abs shot-cap" style="left:870px">Lorem Ipsum Dolor Sit</div>

<!-- testimonials -->
<h2 class="abs heading testi-title"><em>CLIENTS</em> TESTIMONIALS</h2>
<div class="divider" style="top:2354px"></div>

<div class="abs avatar" style="left:80px;top:2420px;background:linear-gradient(160deg,#d9c8b8,#8d7d70)" role="img" aria-label="Portrait of client Mr. Alan Corbet"></div>
<p class="abs quote" style="left:214px;top:2426px;width:356px"><span class="mark">“</span>Lorem ipsum dolor sit amet, consectet uer adipiscing elit, sed diam nonummy nibh euis mod tincidun nt ut laoreetml dolore magna aliquam erat volutpat. Ut wisi enim ad minim veniam, quis nostrud exer.</p>
<div class="abs testi-rule" style="left:80px;top:2560px;width:480px"></div>
<div class="abs who" style="left:436px;top:2573px">- Mr. Alan Corbet</div>

<div class="abs avatar" style="left:632px;top:2420px;background:linear-gradient(160deg,#b9c6d4,#5f7286)" role="img" aria-label="Portrait of client Mr. Tom Harlow"></div>
<p class="abs quote" style="left:766px;top:2426px;width:356px"><span class="mark">“</span>Lorem ipsum dolor sit amet, consectet uer adipiscing elit, sed diam nonummy nibh euis mod tincidun nt ut laoreetml dolore magna aliquam erat volutpat. Ut wisi enim ad minim veniam, quis nostrud exer.</p>
<div class="abs testi-rule" style="left:632px;top:2560px;width:480px"></div>
<div class="abs who" style="left:980px;top:2573px">- Mr. Tom Harlow</div>
<div class="abs pager"><i class="on"></i><i></i><i></i></div>

<!-- contact -->
<section class="abs contact">
  <div class="notch" style="top:0;border-top:22px solid var(--white)"></div>
</section>
<h2 class="abs heading contact-title">CONTACT US</h2>
<div class="divider on-dark" style="top:2772px"></div>
<p class="abs contact-sub">Come on by! We'd love to see you</p>
<div class="abs contact-rule"></div>

<div class="abs col-title" style="left:100px;top:2866px">Quick Contact</div>
<div class="abs field" style="top:2902px">Name</div>
<div class="abs field" style="top:2934px">Email</div>
<div class="abs field" style="top:2966px">Phone</div>
<div class="abs field" style="top:2998px;height:78px">Message</div>
<div class="abs send">SEND</div>

<div class="abs col-title" style="left:470px;top:2862px">Find Us</div>
<div class="abs info" style="top:2904px"><svg width="12" height="16" viewBox="0 0 12 16"><path d="M6 0a6 6 0 0 1 6 6c0 4-6 10-6 10S0 10 0 6a6 6 0 0 1 6-6z" fill="#ccc"/><circle cx="6" cy="6" r="2" fill="#222"/></svg><span><b>QUILL BROTHERS</b><br>37 Carrow Lane, Petone, Wellington</span></div>
<div class="abs info" style="top:2958px"><svg width="14" height="14" viewBox="0 0 14 14"><path d="M3 1l2 3-1.5 1.5a8 8 0 0 0 5 5L10 9l3 2-1.5 2.5C6 13 1 8 .5 2.5z" fill="#ccc"/></svg><b>022 418 3961</b></div>
<div class="abs info" style="top:2988px"><svg width="14" height="14" viewBox="0 0 14 14"><rect x="3" y="0" width="8" height="4" fill="#ccc"/><rect x="0" y="4" width="14" height="7" rx="1" fill="#ccc"/><rect x="3" y="9" width="8" height="5" fill="#ccc"/></svg><b>022 418 3961</b></div>
<div class="abs info" style="top:3018px"><svg width="14" height="11" viewBox="0 0 14 11"><rect x="0" y="0" width="14" height="11" fill="#ccc"/><path d="M0 0l7 6 7-6" fill="none" stroke="#222" stroke-width="1.4"/></svg>merit.h@qbroltd.co.nz</div>
<div class="abs socials"><i></i><i></i><i></i><i></i></div>

<div class="abs contact-brand">QUILL</div>
<div class="abs contact-brand-sub">BROTHERS</div>

<!-- newsletter -->
<section class="abs newsletter"></section>
<div class="abs nl-icon"><svg width="26" height="20" viewBox="0 0 26 20"><rect x="1.5" y="1.5" width="23" height="17" fill="none" stroke="#fff" stroke-width="2.5"/><path d="M1.5 1.5l11.5 9 11.5-9" fill="none" stroke="#fff" stroke-width="2.5"/></svg></div>
<div class="abs nl-title">Sign Up For Newsletter</div>
<div class="abs nl-input">Enter your email here</div>
<div class="abs nl-btn">SUBSCRIBE</div>

<footer class="abs footer">Copyright © 2016 Quill Brothers. All Rights Reserved.</footer>

</body>
</html>
```